Dermiva clinic Website for young modern clinic

Website for dermiva clinic
To be modern and sleek.
Clinic base - are young and modern.
Images
Main treatments are Dermiva and lip enhancement
Needs to include
Link to Facebook
Link to twitter
Price list
Room for a small brief on each item
Hours
Mon 10-4pm
Tues 10-4pm
Wed 12-8pm
Thurs Quenby Row 0700-4pm
Friday 10- 2pm
Saturday 9am - 2pm
Booking page/calender
Where we are - map
Address:
52 Wexmoor Lane, 4 Fenbrook Parade TN9 4QW
Phone number 0207 384 9102 or 07914385217
Company Name: NPA
Address: 52 Wexmoor Lane, 4 Fenbrook Parade, TN9 4QW
Phone: 0207 384 9102
Website: www.nessapelbourneaesthetics.co.uk
Clinic
3 page

```html
<!DOCTYPE html>
<html lang="en">
<head>
<meta charset="utf-8">
<title>Nessa Pelbourne Aesthetics</title>
<link rel="stylesheet" href="https://fonts.googleapis.com/css2?family=Merriweather:wght@400;700&family=Great+Vibes&family=Arimo:wght@400;700&display=swap">
<style>
:root{
  --ink:#333333;
  --ink-soft:#555555;
  --muted:#777777;
  --line:#dddddd;
  --band:#f4f4f4;
  --hero-a:#f2f2f2;
  --hero-b:#c9c9c9;
  --skin:#c9a690;
  --dark:#222222;
  --footer:#efefef;
  --bar:#333333;
  --button:#999999;
  --blue:#3a5fc0;
  --map:#e6e2da;
  --white:#ffffff;
}
*{margin:0;padding:0;box-sizing:border-box}
html,body{width:1200px;height:2490px;overflow:hidden}
body{position:relative;background:var(--white);color:var(--ink);font-family:"Arimo",Arial,sans-serif}
.abs{position:absolute}
.serif{font-family:"Merriweather",Georgia,serif}

/* hero */
.hero{left:0;top:0;width:1200px;height:656px;background:linear-gradient(100deg,var(--hero-a) 0%,#dcdcdc 45%,var(--hero-b) 100%)}
.hero-photo{right:0;top:0;width:560px;height:656px;background:radial-gradient(ellipse at 60% 45%,#e3c4ad 0%,#cdb3a2 35%,rgba(200,200,200,0) 70%)}
.brand{left:78px;top:17px;width:230px;text-align:center}
.brand-mark{width:80px;height:80px;border-radius:50%;border:3px solid var(--dark);margin:0 auto 14px}
.brand-name{font-family:"Merriweather",Georgia,serif;font-size:19px;line-height:24px;letter-spacing:2px;color:var(--dark)}
.nav{left:418px;top:50px;display:flex;gap:0;font-family:"Merriweather",Georgia,serif;font-size:14px;color:var(--ink)}
.nav a{color:inherit;text-decoration:none;margin-right:34px;padding-bottom:12px}
.nav a.current{border-bottom:1px solid var(--ink)}
.hero-script{left:78px;top:255px;font-family:"Great Vibes",cursive;font-size:46px;line-height:72px;color:var(--ink)}
.hero-cta{left:78px;top:412px;font-family:"Merriweather",Georgia,serif;font-size:21px;color:var(--ink-soft)}
.hero-phone{left:78px;top:452px;font-family:"Merriweather",Georgia,serif;font-size:34px;color:var(--ink-soft)}
.dots{left:530px;top:603px;display:flex;gap:15px}
.dots span{width:16px;height:16px;border:1.5px solid var(--ink-soft);border-radius:50%}
.dots span.on{background:radial-gradient(circle,var(--ink-soft) 35%,transparent 40%)}

/* welcome */
.welcome-title{left:78px;top:712px;font-size:33px;color:var(--ink)}
.welcome-text{left:78px;top:768px;width:600px;font-size:14.5px;line-height:23px;color:var(--ink-soft)}
.welcome-text p{margin-bottom:23px}
.btn-outline{left:78px;top:979px;width:144px;height:50px;border:2px solid var(--ink-soft);font-size:16px;display:flex;align-items:center;justify-content:center;color:var(--ink)}
.hours{left:852px;top:686px;width:212px;text-align:center}
.hours-title{font-size:20px;font-weight:700;margin:26px 0 12px;color:var(--dark)}
.hours li{list-style:none;font-size:14px;color:var(--ink-soft);padding:9px 0;border-bottom:1px solid var(--line);line-height:18px}
.hours li:last-child{border-bottom:none}
.hours small{display:block;font-size:9px;color:var(--muted);line-height:10px}

/* appointment band */
.band{left:78px;top:1084px;width:1044px;height:186px;background:var(--band);border-bottom:3px solid var(--button)}
.band-lead{left:32px;top:42px;font-size:29px;color:var(--ink-soft)}
.band-title{left:32px;top:86px;font-size:42px;color:var(--ink-soft)}
.btn-solid{right:63px;top:68px;width:144px;height:50px;background:var(--button);color:var(--white);font-size:16px;display:flex;align-items:center;justify-content:center;letter-spacing:1px}

/* treatments */
.section-title{left:0;width:1200px;top:1312px;text-align:center;font-size:43px;color:var(--ink-soft)}
.card{left:418px;top:1386px;width:364px;height:362px;background:linear-gradient(160deg,#c8a996 0%,#b89583 55%,#8f7466 100%)}
.card-info{left:0;bottom:0;width:364px;height:102px;background:rgba(40,34,30,.8);color:var(--white)}
.card-name{left:35px;top:28px;font-size:32px}
.card-prices{left:218px;top:20px;font-size:14px;line-height:22px}
.card-prices li{list-style:disc}
.arrow{top:1560px}

/* map */
.map{left:0;top:1803px;width:1200px;height:259px;background:linear-gradient(135deg,#ebe7df,var(--map))}

/* newsletter */
.newsletter{left:78px;top:1979px;width:1044px;height:207px;background:var(--dark);color:var(--white);text-align:center}
.news-title{left:0;width:1044px;top:40px;font-size:25px}
.news-sub{left:0;width:1044px;top:80px;font-size:15px}
.news-input{left:241px;top:113px;width:375px;height:55px;background:var(--white);color:var(--dark);font-size:15px;padding-left:23px;display:flex;align-items:center}
.news-btn{left:616px;top:113px;width:187px;height:55px;background:var(--blue);font-size:19px;display:flex;align-items:center;justify-content:center}

/* footer */
.footer{left:0;top:2062px;width:1200px;height:376px;background:var(--footer)}
.footer-brand{left:170px;top:2258px;width:162px;text-align:center}
.footer-brand .brand-mark{width:48px;height:48px;border:2px solid #8a8a8a;margin-bottom:10px}
.footer-brand .brand-name{font-size:13px;line-height:17px;color:#8a8a8a;letter-spacing:1.5px}
.foot-head{font-size:20px;color:var(--ink)}
.foot-links{font-size:14px;color:var(--ink-soft);line-height:31.5px}
.contact-row{left:793px;display:flex;gap:14px;font-size:14px;line-height:22px;color:var(--ink-soft)}
.contact-row svg{flex:none}
.bottom-bar{left:0;top:2438px;width:1200px;height:52px;background:var(--bar);color:var(--white);display:flex;align-items:center;padding-left:78px;font-family:"Merriweather",Georgia,serif;font-size:14.5px}
.bottom-bar u{text-underline-offset:3px}
.social{right:85px;top:2456px;display:flex;gap:16px}
.social span{width:14px;height:14px;border-radius:50%;background:#bbbbbb}
</style>
</head>
<body>

<section class="abs hero" role="img" aria-label="Soft grey studio photograph of a smiling woman with a lily in her hair and a dancer in flowing white behind her"></section>
<div class="abs hero-photo" aria-hidden="true"></div>

<div class="abs brand">
  <div class="brand-mark"></div>
  <div class="brand-name">NESSA PELBOURNE<br>AESTHETICS</div>
</div>

<nav class="abs nav">
  <a class="current" href="#">HOME</a>
  <a href="#">TREATMENTS</a>
  <a href="#">COSMETIC SURGERY</a>
  <a href="#">PRICE LIST</a>
  <a href="#">GALLERY</a>
  <a href="#" style="margin-right:0">CONTACT</a>
</nav>

<div class="abs hero-script">Achieve a<br>Fresh &amp; Beautiful You.</div>
<div class="abs hero-cta">BOOK AN APPOINTMENT NOW</div>
<div class="abs hero-phone">0207 384 9102 or 07914385217</div>
<div class="abs dots"><span></span><span class="on"></span><span></span><span></span><span></span></div>

<h1 class="abs serif welcome-title" style="font-weight:400">WELCOME to Nessa Pelbourne Aesthetics</h1>
<div class="abs welcome-text">
  <p>Nessa is a registered nurse and independent nurse prescriber with over 7 years experience in cosmetic medicine and facial injections.</p>
  <p>She is a member of the ACPN, NRC and insured with Ashby and Grove. She has worked with top plastic surgeons and dermatologists in NZ, Australia and the UK including Quenby Row.</p>
  <p>Nessa will help you look your best and achieve a fresh and beautiful you.</p>
</div>
<a class="abs btn-outline" href="#" style="text-decoration:none">Know More</a>

<aside class="abs hours">
  <svg width="90" height="50" viewBox="0 0 90 50" style="position:absolute;left:61px;top:-2px" aria-hidden="true">
    <g stroke="#bbbbbb" stroke-width="3" stroke-linecap="round">
      <line x1="45" y1="4" x2="45" y2="14"/><line x1="27" y1="8" x2="31" y2="17"/><line x1="63" y1="8" x2="59" y2="17"/>
      <line x1="14" y1="18" x2="21" y2="24"/><line x1="76" y1="18" x2="69" y2="24"/>
    </g>
  </svg>
  <div class="hours-title serif">OUR TIME</div>
  <ul>
    <li>Monday - 10AM to 4PM</li>
    <li>Tuesday - 10AM to 4PM</li>
    <li>Wednesday - 12PM to 8PM</li>
    <li>Thursday - 7:30PM to 4:30PM<small>@ Quenby Row Only</small></li>
    <li>Friday - 10AM to 2PM</li>
    <li>Saturday - 9AM to 2PM</li>
    <li>Sunday - Closed</li>
  </ul>
</aside>

<section class="abs band">
  <div class="abs serif band-lead">If You Need Us ?</div>
  <div class="abs serif band-title">MAKE AN APPOINTMENT NOW</div>
  <a class="abs btn-solid" href="#" style="text-decoration:none">BOOK &nbsp;NOW</a>
</section>

<h2 class="abs serif section-title" style="font-weight:400">Tretments</h2>
<svg class="abs arrow" style="left:174px" width="16" height="30" viewBox="0 0 16 30" aria-hidden="true"><polyline points="13,3 3,15 13,27" fill="none" stroke="#aaaaaa" stroke-width="2"/></svg>
<svg class="abs arrow" style="left:1010px" width="16" height="30" viewBox="0 0 16 30" aria-hidden="true"><polyline points="3,3 13,15 3,27" fill="none" stroke="#222222" stroke-width="2.5"/></svg>
<article class="abs card" role="img" aria-label="Photograph of a woman receiving a Dermiva injection to the forehead">
  <div class="abs card-info">
    <div class="abs serif card-name">DERMIVA</div>
    <ul class="abs card-prices">
      <li>1 Area - £100</li>
      <li>2 Areas - £150</li>
      <li>3 Areas - £200</li>
    </ul>
  </div>
</article>

<section class="abs map" role="img" aria-label="Street map showing the clinic location at 4 Fenbrook Parade"></section>

<section class="abs footer"></section>

<section class="abs newsletter">
  <div class="abs serif news-title">NEWSLETTER</div>
  <div class="abs serif news-sub">Enter Your E-Mail Address for Getting Updates</div>
  <div class="abs news-input">Email-Address</div>
  <div class="abs news-btn">Subscribe</div>
</section>

<div class="abs footer-brand">
  <div class="brand-mark"></div>
  <div class="brand-name">NESSA PELBOURNE<br>AESTHETICS</div>
</div>

<div class="abs serif foot-head" style="left:488px;top:2210px">Navigation Links</div>
<div class="abs foot-links" style="left:488px;top:2250px">Home<br>Tretments<br>Cosmetic Surgery<br>Price List<br>Contact</div>
<div class="abs foot-links" style="left:634px;top:2250px">Gallery<br>Blog<br>Terms<br>Faq's</div>

<div class="abs serif foot-head" style="left:793px;top:2210px">Contact us</div>
<div class="abs contact-row" style="top:2254px">
  <svg width="26" height="30" viewBox="0 0 26 30" aria-hidden="true"><path d="M13 2a9 9 0 0 0-9 9c0 7 9 17 9 17s9-10 9-17a9 9 0 0 0-9-9z" fill="none" stroke="#777" stroke-width="1.6"/><circle cx="13" cy="11" r="3.2" fill="none" stroke="#777" stroke-width="1.6"/></svg>
  <span style="width:260px">52 Wexmoor Lane, 4 Fenbrook Parade TN9 4QW</span>
</div>
<div class="abs contact-row" style="top:2318px">
  <svg width="26" height="22" viewBox="0 0 26 22" aria-hidden="true"><path d="M5 3l4 0 2 5-3 2c1 3 4 6 7 7l2-3 5 2v4c0 1-1 2-2 2C11 22 3 14 3 5c0-1 1-2 2-2z" fill="none" stroke="#777" stroke-width="1.6"/></svg>
  <span>0207 384 9102, 07914 385 217</span>
</div>
<div class="abs contact-row" style="top:2359px">
  <svg width="26" height="22" viewBox="0 0 26 22" aria-hidden="true"><rect x="3" y="5" width="19" height="13" fill="none" stroke="#777" stroke-width="1.6"/><polyline points="3,5 12.5,12 22,5" fill="none" stroke="#777" stroke-width="1.6"/></svg>
  <span>bookings@nessapelbourne.co.uk</span>
</div>

<footer class="abs bottom-bar">© &nbsp;<u>Nessa Pelbourne Aesthetics</u>&nbsp;– 2015 All rights reserved</footer>
<div class="abs social" aria-label="Social links"><span></span><span></span><span></span><span></span></div>

</body>
</html>
```